Portal Bolts Prime

THIS IS A DESIGN & BUILD COMPETITION

Im Looking for a fresh E-commerce website to sell door locks, I would like it to be more visually based, so instead of having worded categories, have then visual, with rim cylinders, euro cylinders, garage locks, oval cylinders, deadlocks, sash locks, Upvc multipoint locks, door handles, window handles, safes, padlocks etc, as picture, with a product manufacturer search feature, a video tab or banner to stream videos,
Updates

Hi Everyone,

Im looking for a fully functioning e-commerce website not a logo

Thanks
Neil

I really like this website http://keenfrontier.com.au/ so make it similar to this with the blues from my logo, I will upload some random stock pictures later

Hi Everyone,

Im overwhelmed by some of the designs which have been great, however I think I need to make my vision clearer, Im looking for 12 - 16 categories - euro cylinders, rim cylinders, sashlocks, deadlocks, door handles, garage locks, safes, multipoint locks, panic hardware, padlocks, nightlatches, Post Boxes.

these are only categories, once the customer clicks on the category they will have a choice of manufacturers which will be between 4/5 Hoxby, Crestor, Ivo, Pan-o-bar, Kilt, Wrexford.

The reason for this is people generally dont know what the lock on their door is called and I want a site to be visual to enable customers to source the locks they need.

This is what will make my site unique!!!!

Colour is important, I want to use the blue from my logo to keep it uniformed

I like the idea of reviewed products down the left hand side

I would like a product/ manufacturer search facility 

All the above are in your designs, but they are not all on 1 design ;0)

Thanks Everyone
Neil

Hi everyone,

Done some paint shop lol with one of the submitted designs just to show yous guys what im looking for

The12 pictures in the main part of the page are categories, not sale items

Thanks

Neil

Reason: I have extended the design period as there has been a misunderstanding with this competition, The competition is for design and build

Hi Everyone,

I have extended this competition as there was a misunderstanding with this project, It is for full design and build of an ecommerce website, not just design, I will put the prize money upto £1000 total fund, so please if you cant build your design then please withdraw them.

Thanks
Neil

Target Market(s)

The market is for DIY customers wanting to change their own locks.

Industry/Entity Type

Garage

Requirements
Must have
• It must be visually based, to help customers identify the product they need,

It must also have a banner/ picture of how to measure a euro cylinder.

I think it would work best if we have a generic category picture, then when you click the picture it then has a manufacturer page in pictures again with a brief description of what the lock offers ie, anti bump, anti snap, anti drill, British Standard etc.

must be easy to populate with stock
Nice to have
• I would like it to have geolocation for visitors ip addresses so I can see where they are staying so I can offer a fitting service.

```html
<!DOCTYPE html>
<html lang="en">
<head>
<meta charset="utf-8">
<title>Portal Bolts Prime</title>
<link href="https://fonts.googleapis.com/css2?family=Open+Sans:wght@400;600;700&family=Oswald:wght@500&display=swap" rel="stylesheet">
<style>
:root{
  --blue:#1b3f9c;--blue-dark:#0f2766;--blue-btn:#1747a6;--ink:#333;--muted:#777;
  --page:#f0f0f0;--panel:#fff;--line:#dedede;--badge:#4d5b86;--brick:#8e3b31;--yellow:#f6c300;--orange:#f39200;--red:#c4161c;
}
*{margin:0;padding:0;box-sizing:border-box}
html,body{width:800px;height:1200px;overflow:hidden}
body{position:relative;background:var(--page);font-family:"Open Sans",sans-serif;color:var(--ink);font-size:7px}
.abs{position:absolute}
.topbar{left:0;top:0;width:800px;height:24px;background:#2f2f2f;color:#ddd;font-size:6px}
.topbar .welcome{left:132px;top:9px}
.topbar .account{right:132px;top:8px}
.header{left:0;top:24px;width:800px;height:79px;background:#ececec}
.brand{left:131px;top:8px;width:86px;color:var(--blue);font-weight:700;font-size:19px;line-height:20px;letter-spacing:-.5px}
.search{left:250px;top:22px;width:418px;height:34px;background:#fff;border-radius:2px}
.search .field{top:9px;height:16px;background:#f2f2f2;border:1px solid #e4e4e4;color:#aaa;font-size:5.5px;padding:4px 5px}
.search .btn{left:317px;top:6px;width:90px;height:19px;background:linear-gradient(#2a5cc8,#163c98);color:#fff;border-radius:3px;text-align:center;font-size:8px;line-height:19px}
.keywords{left:250px;top:62px;font-size:5.5px;color:#666}
.nav{left:126px;top:112px;width:548px;height:34px;background:linear-gradient(90deg,#1e3f95,#143281 60%,#1f47a8);border-radius:2px;color:#fff;font-size:8px}
.nav ul{list-style:none;display:flex;gap:18px;position:absolute;left:17px;top:12px}
.nav .phone{right:13px;top:6px;color:var(--yellow);font-weight:700;font-size:12px;text-align:right;line-height:13px}
.nav .phone small{display:block;color:#fff;font-weight:400;font-size:5.5px;line-height:8px}
.hero{left:126px;top:158px;width:548px;height:192px;background:var(--brick)}
.hero .door{left:0;top:0;width:194px;height:192px;background:linear-gradient(90deg,#c9bfb0,#e6e1d8 50%,#9c3d30)}
.hero .video{left:195px;top:24px;width:280px;height:142px;background:#fff;padding:5px}
.hero .screen{width:100%;height:100%;background:linear-gradient(#4c6b3c,#7d9a6a 60%,#394c2c)}
.hero .play{left:108px;top:30px;width:44px;height:32px;background:rgba(0,0,0,.55);border-radius:4px}
.hero .bar{height:14px;background:rgba(0,0,0,.75)}
.hero .mark{left:486px;top:22px;color:#fff;font-size:12px;line-height:13px;font-weight:400}
.hero .dots{left:13px;top:179px;display:flex;gap:2px}
.hero .dots i{width:7px;height:7px;border-radius:50%;background:#555;border:1px solid #ddd}
.hero .dots i:first-child{background:#fff}
.cats{left:126px;top:362px;width:548px;height:76px;background:#fff}
.arrow{width:16px;height:16px;border-radius:50%;background:#333}
.cats .list{left:42px;top:12px;display:flex;gap:10px}
.cat{width:48px;text-align:center;font-size:5px;color:#555}
.cat .pic{width:40px;height:34px;margin:0 auto 6px;border-radius:4px;background:linear-gradient(#d9d9d9,#9a9a9a)}
.content{left:126px;top:446px;width:548px;height:552px;background:#fff}
.promo-side{left:131px;top:458px;width:127px;height:127px;border:1px solid #999;background:#fff;overflow:hidden}
.promo-side .name{left:8px;top:5px;color:var(--red);font-weight:700;font-size:11px}
.promo-side .pic{left:8px;top:21px;width:110px;height:54px;background:linear-gradient(#b8bec8,#3a3f48);border-radius:6px}
.promo-side .cap{left:8px;top:78px;font-size:6px;line-height:8px}
.promo-side .foot{left:0;top:91px;width:125px;height:34px;background:var(--red);color:#fff;font-size:6.6px;padding:6px 6px 0;line-height:10px;letter-spacing:-.1px}
.side-box{left:131px;width:127px;background:#f5f5f5}
.side-box h3{font-weight:400;font-size:9px;color:var(--blue);margin:10px 10px 6px}
.news li{list-style:none;position:relative;padding:0 8px 0 22px;margin-bottom:10px;font-size:5.5px;color:#888;line-height:9px}
.news li:before{content:"";position:absolute;left:10px;top:2px;width:5px;height:5px;border-radius:50%;background:#1f86d4}
.news b{display:block;color:#444;font-weight:600}
.deal-input{margin:5px 6px;height:16px;background:#fff;border:1px solid #e5e5e5}
.deal-btn{margin:6px auto 0;width:54px;height:11px;background:linear-gradient(#ffb03b,#f07c00);color:#fff;font-size:6px;text-align:center;line-height:11px;border-radius:2px}
.sec-title{font-size:9px;color:#444}
.pager{display:flex;gap:2px}
.pager i{width:9px;height:9px;border-radius:50%;background:#222}
.grid{left:269px;display:grid;grid-template-columns:repeat(3,126px);column-gap:11px}
.card{height:110px;border:1px solid var(--line);position:relative;text-align:center;background:#fff}
.card .pic{position:absolute;left:28px;top:22px;width:52px;height:44px;border-radius:6px;background:linear-gradient(#e7cf6a,#9b7a1c)}
.card .pic.silver{background:linear-gradient(#e8e8e8,#8c8c8c)}
.card .pic.dark{background:linear-gradient(#b9b9b9,#4b4b4b)}
.badge{position:absolute;right:6px;top:5px;width:39px;height:39px;border-radius:50%;background:var(--badge);color:#fff;font-size:10px;font-weight:600;line-height:11px;padding-top:8px}
.card .title{position:absolute;left:0;right:0;top:76px;font-size:9px;color:#555}
.card .price{position:absolute;left:0;right:0;top:88px;font-size:9.5px;font-weight:700;color:var(--blue)}
.btns{display:flex;gap:2px;justify-content:center;height:16px}
.btns span{height:16px;line-height:16px;font-size:6.5px;color:#fff;text-align:center}
.btns .info{width:52px;background:var(--blue-btn)}
.btns .buy{width:54px;background:#2f2f2f}
.stars{display:flex;justify-content:center;align-items:center;gap:1px;font-size:6px;color:#555;height:12px}
.stars svg{width:9px;height:9px}
.ribbon{height:40px;background:linear-gradient(#1d4bb0,#163a8d);color:#fff;font-family:"Oswald",sans-serif;font-size:11px;position:relative;padding:14px 0 0 13px}
.ribbon i{position:absolute;right:6px;top:-4px;width:36px;height:40px;border-radius:6px}
.footer-col{top:1018px;font-size:6.5px;color:#444}
.footer-col h4{font-weight:400;font-size:9px;color:var(--blue);margin-bottom:12px}
.footer-col li{list-style:none;margin-bottom:8px}
.social li{display:flex;justify-content:space-between;align-items:center;width:122px;margin-bottom:8px}
.social i{width:16px;height:16px;border-radius:50%;background:var(--blue);display:block}
.cards-pay{left:563px;top:1117px;display:flex;gap:3px}
.cards-pay span{width:26px;height:13px;border:1px solid #ccc;background:#fff;font-size:5px;text-align:center;line-height:11px;color:var(--blue);font-weight:600}
.copy{left:0;width:800px;top:1170px;text-align:center;font-size:6.5px;color:#555}
</style>
</head>
<body>
<div class="abs topbar">
  <span class="abs welcome">Welcome to PortalBoltsPrime.com.au</span>
  <span class="abs account">My Account &nbsp;|&nbsp; &nbsp;Login or Register &nbsp;| &nbsp;Cart ( 0 item )</span>
</div>

<header class="abs header">
  <div class="abs brand">PORTAL BOLTS PRIME</div>
  <div class="abs search">
    <div class="abs field" style="left:11px;width:180px">Search Product</div>
    <div class="abs field" style="left:203px;width:100px">All Department</div>
    <div class="abs btn">Search</div>
  </div>
  <div class="abs keywords">Popular Keywords : rim cylinders, euro cylinders, garage locks, oval cylinders, deadlocks, sash locks, Upvc multipoint locks, door handles, window handles etc..</div>
</header>

<nav class="abs nav">
  <ul><li>Home</li><li>New Arrivals</li><li>Free Shipping</li><li>Clearance</li><li>F.A.Q</li><li>News</li><li>About Us</li></ul>
  <div class="abs phone">1-800-555-017<small>Free shipping for all Products</small></div>
</nav>

<section class="abs hero">
  <div class="abs door" role="img" aria-label="Living room doorway with a tall chrome door handle"></div>
  <div class="abs video">
    <div class="screen" role="img" aria-label="Video still of a patio with open glass doors"></div>
    <div class="abs play"><svg width="44" height="32"><polygon points="18,9 29,16 18,23" fill="#fff"/></svg></div>
    <div class="abs bar" style="left:5px;bottom:5px;width:270px"><svg width="270" height="14"><polygon points="16,4 22,7 16,10" fill="#fff"/><rect x="50" y="6" width="190" height="2" fill="#666"/><rect x="50" y="6" width="100" height="2" fill="#2a7be4"/></svg></div>
  </div>
  <div class="abs mark">PORTAL<br>BOLTS<br>PRIME</div>
  <div class="abs dots"><i></i><i></i><i></i><i></i></div>
</section>

<section class="abs cats">
  <div class="abs arrow" style="left:10px;top:24px"><svg width="16" height="16"><polyline points="10,4 6,8 10,12" fill="none" stroke="#fff" stroke-width="2"/></svg></div>
  <div class="abs list">
    <div class="cat"><div class="pic" role="img" aria-label="Rim cylinder"></div>Rim Cylinders</div>
    <div class="cat"><div class="pic" role="img" aria-label="Euro cylinder"></div>Euro Cylinders</div>
    <div class="cat"><div class="pic" role="img" aria-label="Garage lock" style="background:linear-gradient(#e85050,#8a1a1a)"></div>Garage Locks</div>
    <div class="cat"><div class="pic" role="img" aria-label="Oval cylinder"></div>Oval cylinders</div>
    <div class="cat"><div class="pic" role="img" aria-label="Deadlock"></div>Deadlocks</div>
    <div class="cat"><div class="pic" role="img" aria-label="Sash lock" style="background:linear-gradient(#f0d06a,#a07a1e)"></div>Sash locks</div>
    <div class="cat"><div class="pic" role="img" aria-label="Door lock handle"></div>Door locks</div>
    <div class="cat" style="width:64px"><div class="pic" role="img" aria-label="Upvc multipoint lock" style="background:linear-gradient(#f0d06a,#a07a1e)"></div>Upvc multipoint locks</div>
  </div>
  <div class="abs arrow" style="left:522px;top:24px"><svg width="16" height="16"><polyline points="6,4 10,8 6,12" fill="none" stroke="#fff" stroke-width="2"/></svg></div>
</section>

<main class="abs content"></main>

<aside>
  <div class="abs promo-side">
    <div class="abs name">HOOKWELL</div>
    <div class="abs pic" role="img" aria-label="Heavy-duty pulley block product"></div>
    <div class="abs cap">The original Hookwell Blocks</div>
    <div class="abs foot">Hookwell Products. Professionals<br>around the world rely on it.</div>
  </div>
  <div class="abs side-box news" style="top:604px;height:168px">
    <h3>Latest News</h3>
    <ul>
      <li>Sed ut perspiciatis unde omnis iste natus error sit voluptatem accus-antium<b>04/26/2013 &nbsp; 10 minutes ago</b></li>
      <li>At vero eos et accusamus et iusto odio dignissimos ducimus qui<b>04/26/2013 &nbsp; 10 minutes ago</b></li>
      <li>We denounce with righteous indignation and dislike men<b>04/26/2013 &nbsp; 10 minutes ago</b></li>
    </ul>
  </div>
  <div class="abs side-box" style="top:792px;height:90px">
    <h3 style="margin-bottom:2px">Get Deals</h3>
    <div style="font-size:5.5px;margin-left:6px">Sign Up for Our Hot Deal Newsletter</div>
    <div class="deal-input"></div>
    <div class="deal-btn">SUBMIT</div>
  </div>
</aside>

<div class="abs sec-title" style="left:267px;top:456px">Featured Products</div>
<div class="abs pager" style="left:649px;top:458px"><i></i><i></i></div>

<div class="abs grid" style="top:475px;row-gap:4px">
  <div class="card"><div class="pic silver" role="img" aria-label="Chrome door knob set"></div><div class="badge">22%<br>off</div><div class="title">Portal Bolt Prime</div><div class="price">$ 150</div></div>
  <div class="card"><div class="pic" role="img" aria-label="Brass door knob"></div><div class="badge">22%<br>off</div><div class="title">Portal Bolt Prime</div><div class="price">$ 150</div></div>
  <div class="card"><div class="pic" role="img" aria-label="Brass deadbolt and knob"></div><div class="badge">22%<br>off</div><div class="title">Portal Bolt Prime</div><div class="price">$ 150</div></div>
  <div class="btns"><span class="info">For More Info</span><span class="buy">Buy Now</span></div>
  <div class="btns"><span class="info">For More Info</span><span class="buy">Buy Now</span></div>
  <div class="btns"><span class="info">For More Info</span><span class="buy">Buy Now</span></div>
</div>
<div class="abs grid" style="top:620px;row-gap:4px">
  <div class="card"><div class="pic dark" role="img" aria-label="T-handle garage lock"></div><div class="badge">22%<br>off</div><div class="title">Portal Bolt Prime</div><div class="price">$ 150</div></div>
  <div class="card"><div class="pic" role="img" aria-label="Brass padlock"></div><div class="badge">22%<br>off</div><div class="title">Portal Bolt Prime</div><div class="price">$ 150</div></div>
  <div class="card"><div class="pic dark" role="img" aria-label="Steel safe"></div><div class="badge">22%<br>off</div><div class="title">Portal Bolt Prime</div><div class="price">$ 150</div></div>
  <div class="btns"><span class="info">For More Info</span><span class="buy">Buy Now</span></div>
  <div class="btns"><span class="info">For More Info</span><span class="buy">Buy Now</span></div>
  <div class="btns"><span class="info">For More Info</span><span class="buy">Buy Now</span></div>
</div>

<div class="abs grid" style="top:760px">
  <div class="ribbon">NEW ARRIVAL<i role="img" aria-label="Red new sticker" style="background:#e53b1f;border-radius:50%;width:38px;height:38px"></i></div>
  <div class="ribbon">CLEARANCE SALE<i role="img" aria-label="Orange shopping bag" style="background:#f06a1c"></i></div>
  <div class="ribbon">FREE SHIPPING<i role="img" aria-label="Red delivery trolley with boxes" style="background:#d6382a"></i></div>
</div>

<div class="abs sec-title" style="left:267px;top:816px">Latest Products</div>
<div class="abs pager" style="left:649px;top:818px"><i></i><i></i></div>

<div class="abs grid" style="top:832px;row-gap:4px">
  <div class="card"><div class="pic" role="img" aria-label="Brass oval cylinder"></div><div class="badge">22%<br>off</div><div class="title">Portal Bolt Prime</div><div class="price">$ 150</div></div>
  <div class="card"><div class="pic silver" role="img" aria-label="White window handles"></div><div class="badge">22%<br>off</div><div class="title">Portal Bolt Prime</div><div class="price">$ 150</div></div>
  <div class="card"><div class="pic silver" role="img" aria-label="Chrome rim cylinder"></div><div class="badge">22%<br>off</div><div class="title">Portal Bolt Prime</div><div class="price">$ 150</div></div>
  <div class="stars"><svg viewBox="0 0 10 10"><polygon points="5,0 6.2,3.6 10,3.6 7,5.9 8.1,9.5 5,7.3 1.9,9.5 3,5.9 0,3.6 3.8,3.6" fill="#f5b400"/></svg><svg viewBox="0 0 10 10"><polygon points="5,0 6.2,3.6 10,3.6 7,5.9 8.1,9.5 5,7.3 1.9,9.5 3,5.9 0,3.6 3.8,3.6" fill="#f5b400"/></svg><svg viewBox="0 0 10 10"><polygon points="5,0 6.2,3.6 10,3.6 7,5.9 8.1,9.5 5,7.3 1.9,9.5 3,5.9 0,3.6 3.8,3.6" fill="#f5b400"/></svg><svg viewBox="0 0 10 10"><polygon points="5,0 6.2,3.6 10,3.6 7,5.9 8.1,9.5 5,7.3 1.9,9.5 3,5.9 0,3.6 3.8,3.6" fill="#f5b400"/></svg><svg viewBox="0 0 10 10"><polygon points="5,0 6.2,3.6 10,3.6 7,5.9 8.1,9.5 5,7.3 1.9,9.5 3,5.9 0,3.6 3.8,3.6" fill="#bbb"/></svg>&nbsp;&nbsp;(1 Reviews)</div>
  <div class="stars"><svg viewBox="0 0 10 10"><polygon points="5,0 6.2,3.6 10,3.6 7,5.9 8.1,9.5 5,7.3 1.9,9.5 3,5.9 0,3.6 3.8,3.6" fill="#f5b400"/></svg><svg viewBox="0 0 10 10"><polygon points="5,0 6.2,3.6 10,3.6 7,5.9 8.1,9.5 5,7.3 1.9,9.5 3,5.9 0,3.6 3.8,3.6" fill="#f5b400"/></svg><svg viewBox="0 0 10 10"><polygon points="5,0 6.2,3.6 10,3.6 7,5.9 8.1,9.5 5,7.3 1.9,9.5 3,5.9 0,3.6 3.8,3.6" fill="#f5b400"/></svg><svg viewBox="0 0 10 10"><polygon points="5,0 6.2,3.6 10,3.6 7,5.9 8.1,9.5 5,7.3 1.9,9.5 3,5.9 0,3.6 3.8,3.6" fill="#f5b400"/></svg><svg viewBox="0 0 10 10"><polygon points="5,0 6.2,3.6 10,3.6 7,5.9 8.1,9.5 5,7.3 1.9,9.5 3,5.9 0,3.6 3.8,3.6" fill="#bbb"/></svg>&nbsp;&nbsp;(1 Reviews)</div>
  <div class="stars"><svg viewBox="0 0 10 10"><polygon points="5,0 6.2,3.6 10,3.6 7,5.9 8.1,9.5 5,7.3 1.9,9.5 3,5.9 0,3.6 3.8,3.6" fill="#f5b400"/></svg><svg viewBox="0 0 10 10"><polygon points="5,0 6.2,3.6 10,3.6 7,5.9 8.1,9.5 5,7.3 1.9,9.5 3,5.9 0,3.6 3.8,3.6" fill="#f5b400"/></svg><svg viewBox="0 0 10 10"><polygon points="5,0 6.2,3.6 10,3.6 7,5.9 8.1,9.5 5,7.3 1.9,9.5 3,5.9 0,3.6 3.8,3.6" fill="#f5b400"/></svg><svg viewBox="0 0 10 10"><polygon points="5,0 6.2,3.6 10,3.6 7,5.9 8.1,9.5 5,7.3 1.9,9.5 3,5.9 0,3.6 3.8,3.6" fill="#f5b400"/></svg><svg viewBox="0 0 10 10"><polygon points="5,0 6.2,3.6 10,3.6 7,5.9 8.1,9.5 5,7.3 1.9,9.5 3,5.9 0,3.6 3.8,3.6" fill="#bbb"/></svg>&nbsp;&nbsp;(1 Reviews)</div>
  <div class="btns"><span class="info">For More Info</span><span class="buy">Buy Now</span></div>
  <div class="btns"><span class="info">For More Info</span><span class="buy">Buy Now</span></div>
  <div class="btns"><span class="info">For More Info</span><span class="buy">Buy Now</span></div>
</div>

<footer>
  <div class="abs footer-col" style="left:131px"><h4>Quick Links</h4><ul><li>Home</li><li>New Arrivals</li><li>Free Shipping</li><li>Clearance</li><li>F.A.Q</li><li>News</li><li>About Us</li></ul></div>
  <div class="abs footer-col" style="left:269px"><h4>Support Links</h4><ul><li style="margin-bottom:6px">Legal Notice</li><li style="margin-bottom:6px">Privacy Policy</li><li style="margin-bottom:6px">Terms &amp; Conditions</li><li>Help</li></ul></div>
  <div class="abs footer-col" style="left:405px"><h4>Contact Us</h4><ul>
    <li style="margin-bottom:6px;color:var(--blue);font-weight:600">Portal Bolts Prime</li>
    <li style="margin-bottom:6px">Linden Parade 48</li><li style="margin-bottom:6px">4021 Marlow</li><li style="margin-bottom:6px">London</li>
    <li style="margin-bottom:6px">Phone: <span style="font-size:9px">+1-800-555-017</span></li>
    <li style="margin-bottom:6px">Telefax: <span style="font-size:9px">+1-800-555-017</span></li>
    <li>Email: info@portalboltsprime.com</li></ul></div>
  <div class="abs footer-col social" style="left:548px"><h4>Connect With Us</h4><ul>
    <li><i></i>Chatter</li><li style="margin-top:4px"><i></i>Friendbook</li><li style="margin-top:4px"><i></i>Workline</li></ul></div>
  <div class="abs cards-pay"><span>Cardix</span><span>Paylon</span><span>Orbix</span><span>Tendro</span></div>
  <div class="abs copy">Copyright ©2013 ,Portal Bolts Prime, All rights reserved</div>
</footer>
</body>
</html>
```